Talvor Visit cards serious but not sad

Hello, I'd like to design my visit cards with the logo Talvor (attached) the following information: Name: Karim Belmadi Title: Mobile Director: 33 (0) 6 72 18 35 09 Phone: 33 (0) 4 58 61 07 92 e-mail: karim.belmadi@talvor-consulting.example address: 17 Rue Marcel Danvin 92400 Courbevoie This visit will be used on the banking institutions and Talvor is a consulting firm. I do not want to have dark background.

Target Market(s)

banks

Contact Information for Business Card

Name : Karim Belmadi
Title : Director
mobile : +33(0)6 72 18 35 09
Phone : +33(0)4 58 61 07 92
e-mail: karim.belmadi@talvor-consulting.example
adresse : 17 Rue marcel Danvin 75999 Valmorin

Requirements
Nice to have
• serious but not sad

```html
<!DOCTYPE html>
<html lang="en">
<head>
<meta charset="utf-8">
<title>Talvor business cards</title>
<link rel="stylesheet" href="https://fonts.googleapis.com/css2?family=Exo+2:wght@500;600&family=Roboto:wght@400;500&display=swap">
<style>
  :root {
    --brand-blue: #285a97;
    --stage: #c4c4c4;
    --card-light: #f1f1f1;
    --ink: #2b2b2b;
    --white: #ffffff;
  }
  * { margin: 0; padding: 0; box-sizing: border-box; }
  html, body { width: 1200px; height: 576px; overflow: hidden; }
  body { background: var(--stage); position: relative; font-family: "Roboto", sans-serif; }

  .card {
    position: absolute;
    top: 138px;
    width: 484px;
    height: 292px;
    border-radius: 11px;
    overflow: hidden;
  }
  .card--front { left: 82px; background: var(--brand-blue); }
  .card--back { left: 602px; width: 481px; height: 291px; background: var(--card-light); }

  .wordmark {
    position: absolute;
    display: flex;
    align-items: center;
    font-family: "Exo 2", sans-serif;
    font-weight: 500;
    letter-spacing: 0.5px;
    line-height: 1;
  }
  .wordmark__dot { border-radius: 50%; flex: none; }

  .card--front .wordmark { left: 97px; top: 94px; color: var(--white); font-size: 56px; }
  .card--front .wordmark__dot { width: 66px; height: 66px; background: var(--white); margin-right: 20px; }

  .website {
    position: absolute;
    left: 0; right: 0; bottom: 15px;
    display: flex; justify-content: center; align-items: center; gap: 12px;
    color: var(--white); font-size: 12.5px;
  }
  .website__rule { width: 60px; height: 2px; background: var(--white); border-radius: 1px; }

  .card--back .wordmark { left: 21px; top: 26px; color: var(--brand-blue); font-size: 36px; }
  .card--back .wordmark__dot { width: 58px; height: 58px; background: var(--brand-blue); margin-right: 6px; }

  .accent-disc {
    position: absolute;
    left: 260px; top: -2px;
    width: 292px; height: 292px;
    border-radius: 50%;
    background: var(--brand-blue);
  }

  .holder { position: absolute; left: 23px; top: 138px; }
  .holder__name { font-family: "Exo 2", sans-serif; font-weight: 600; font-size: 22px; color: var(--brand-blue); line-height: 1.1; }
  .holder__title { font-size: 10.5px; color: var(--ink); margin-top: 3px; }

  .contacts { position: absolute; left: 27px; top: 199px; list-style: none; font-size: 12.5px; color: var(--ink); }
  .contacts li { display: flex; align-items: center; height: 16.5px; }
  .contacts svg { width: 10px; height: 10px; margin-right: 9px; fill: var(--brand-blue); flex: none; }
  .address { position: absolute; left: 23px; top: 252px; font-size: 12.5px; color: var(--ink); }
</style>
</head>
<body>
  <section class="card card--front" aria-label="Card front">
    <div class="wordmark"><span class="wordmark__dot"></span>talvor</div>
    <div class="website">
      <span class="website__rule"></span>
      <span>www.talvor-consulting.example</span>
      <span class="website__rule"></span>
    </div>
  </section>

  <section class="card card--back" aria-label="Card back">
    <div class="accent-disc"></div>
    <div class="wordmark"><span class="wordmark__dot"></span>talvor</div>

    <div class="holder">
      <p class="holder__name">Karim Belmadi</p>
      <p class="holder__title">Director</p>
    </div>

    <ul class="contacts">
      <li>
        <svg viewBox="0 0 10 10" aria-hidden="true"><path d="M2.5 0h5a1 1 0 0 1 1 1v8a1 1 0 0 1-1 1h-5a1 1 0 0 1-1-1V1a1 1 0 0 1 1-1zm.5 1.5v6h4v-6z"/></svg>
        +33(0)6 72 18 35 09
      </li>
      <li>
        <svg viewBox="0 0 10 10" aria-hidden="true"><path d="M0 3.5C0 2 2 1 5 1s5 1 5 2.5V5H7.5V3.8h-5V5H0zM2 5.5h6L9.5 9h-9z"/></svg>
        +33(0)4 58 61 07 92
      </li>
      <li>
        <svg viewBox="0 0 10 10" aria-hidden="true"><path d="M0 2h10v.6L5 6 0 2.6zm0 1.8 5 3.4 5-3.4V8H0z"/></svg>
        karim.belmadi@talvor-consulting.example
      </li>
    </ul>
    <p class="address">17 Rue marcel Danvin 75999 Valmorin</p>
  </section>
</body>
</html>
```